Welcome Card Project for bow tie business

We need a welcome message card that will be placed inside a box (packaging) for a mens bow tie business 'Dorian Vellum'. Dorian Vellum is a men's brand specializing in unique bow ties of limited editions using quality designer fabrics.
Dorian Vellum is all about colour, prints and style, where the consumer can add a something a little out of the ordinary and quirky to break out of the mundane 9-5 day.

The dimensions of the double sided welcome card is as follows:
60mm H x 120mm W

One side of the welcome card will have the welcome message with colour and graphics in the background depicting happiness and excitement. It will also include the Chatterbook, quiller and Snapgrove logos and an invitation for customers to share pictures of them wearing the bow ties on Snapgrove and chatterbook. The website address will also be included here (www.dorianvellum.example)

The other side of the welcome card will be more conservative with a black on black paisley print design with the 'Dorian Vellum' logo in a deep purple colour.

Target Market(s)

Men, hipsters, fashionistas, working professionals, women seeking gifts for men

Industry/Entity Type

Conservative

Requirements
Must have
• - Double sided welcome card
- The welcome message (file attached) on one side of the card
- Chatterbook + Snapgrove logo
- Dorian Vellum website address (www.dorianvellum.example)
- Corporate colours: purple, black, orange (on website and in logo) + neutral recycled brown (packaging colour)
- Black on black paisley print on one side of the card
- Dorian Vellum logo (file attached)- colour: deep purple
Nice to have

Should not have
• - pictures of rainbows

```html
<!DOCTYPE html>
<html lang="en">
<head>
<meta charset="utf-8">
<title>Dorian Vellum – Welcome Card</title>
<link rel="stylesheet" href="https://fonts.googleapis.com/css2?family=Crimson+Pro:wght@600;700&family=Roboto+Condensed:wght@700&family=Oswald:wght@500&display=swap">
<style>
  :root {
    --canvas: #ffffff;
    --pattern-pink: #e8406a;
    --pattern-dark: #c93a5c;
    --card-light: #ff5b78;
    --card-mid: #fb5a74;
    --card-deep: #ff3a62;
    --rule-purple: #4d1450;
    --ornament-purple: #7a2a66;
    --message-berry: #a81b4f;
    --gold-light: #f3d9a4;
    --gold-deep: #c9924a;
    --badge-red: #b3283e;
    --white: #ffffff;
  }
  * { margin: 0; padding: 0; box-sizing: border-box; }
  html, body { width: 1115px; height: 1200px; overflow: hidden; background: var(--canvas); }
  .canvas { position: relative; width: 1115px; height: 1200px; }

  .card { position: absolute; left: 117px; width: 886px; height: 465px; }
  .card--front { top: 60px; }
  .card--back { top: 638px; }

  .card__pattern {
    position: absolute; inset: 0;
    background: linear-gradient(135deg, var(--pattern-pink), var(--pattern-dark) 50%, var(--pattern-pink));
  }
  .card__panel {
    position: absolute; left: 33px; top: 35px; width: 818px; height: 397px;
    border-radius: 38px;
    background: linear-gradient(90deg, var(--card-mid) 0%, var(--card-light) 35%, var(--card-light) 65%, var(--card-deep) 100%);
  }

  .rule {
    position: absolute; left: 37px; width: 812px; height: 3px; background: var(--rule-purple);
    z-index: 1;
  }
  .rule--top { top: 98px; }
  .rule--bottom { top: 365px; }

  .flourish {
    position: absolute; left: 396px; width: 80px;
    background: var(--ornament-purple); opacity: .35; z-index: 1;
  }
  .flourish--top { top: 52px; height: 40px; border-radius: 20px 20px 4px 4px; }
  .flourish--bottom { top: 374px; height: 46px; border-radius: 4px 4px 23px 23px; }

  .welcome-seal {
    position: absolute; left: 66px; top: 40px; width: 104px; height: 104px; border-radius: 50%;
    background: radial-gradient(circle at 40% 35%, var(--gold-light), var(--gold-deep));
    display: flex; align-items: center; justify-content: center;
    z-index: 2; box-shadow: 0 0 0 1px rgba(255,255,255,.4);
  }
  .welcome-seal__inner {
    width: 84px; height: 84px; border-radius: 50%;
    background: radial-gradient(circle at 40% 40%, #f2cf8f, #d59d55);
    border: 2px solid #fbe7bf;
    display: flex; align-items: center; justify-content: center;
    font-family: "Crimson Pro", Georgia, serif; font-weight: 700; font-size: 11px;
    letter-spacing: .5px; color: var(--badge-red);
  }

  .headline {
    position: absolute; left: 0; right: 0; top: 108px; text-align: center;
    font-family: "Crimson Pro", Georgia, serif; font-weight: 600; font-size: 36px;
    letter-spacing: 2px; color: var(--white); line-height: 1;
  }
  .message {
    position: absolute; left: 37px; right: 37px; top: 158px; text-align: center;
    font-family: "Crimson Pro", Georgia, serif; font-weight: 700; font-size: 29px;
    line-height: 33px; color: var(--message-berry);
  }
  .message p + p { margin-top: 5px; line-height: 39px; }

  .signoff {
    position: absolute; right: 60px; top: 377px;
    font-family: "Roboto Condensed", Arial, sans-serif; font-weight: 700; font-size: 26px;
    color: var(--white);
  }

  .brand-name {
    position: absolute; left: 0; right: 0; top: 140px; text-align: center;
    font-family: "Crimson Pro", Georgia, serif; font-weight: 600; font-size: 118px;
    line-height: 1; color: var(--white);
  }
  .web-address {
    position: absolute; left: 0; right: 0; top: 402px; text-align: center;
    font-family: "Oswald", "Arial Narrow", sans-serif; font-weight: 500; font-size: 21px;
    color: var(--rule-purple); letter-spacing: .3px;
  }
  .social-names {
    position: absolute; right: 46px; top: 388px; text-align: right;
    font-family: "Roboto Condensed", Arial, sans-serif; font-weight: 700; font-size: 13px;
    line-height: 16px; color: var(--white);
  }
</style>
</head>
<body>
<main class="canvas">

  <section class="card card--front" aria-label="Welcome card, message side">
    <div class="card__pattern" role="img" aria-label="Border of small pink and black hexagon pattern"></div>
    <div class="card__panel"></div>
    <div class="flourish flourish--top" role="img" aria-label="Purple scroll ornament"></div>
    <div class="rule rule--top"></div>
    <div class="welcome-seal"><div class="welcome-seal__inner">WELCOME</div></div>
    <h1 class="headline">THIS IS ONLY THE BEGINNING</h1>
    <div class="message">
      <p>Your Dorian Vellum bow tie is an adventure for you to unfold, unexpected and new.</p>
      <p>Wear it on a night out, or bring a dash of colour to work, dream with it, wear it on a rainy day, create new memories and be surprised.</p>
    </div>
    <div class="rule rule--bottom"></div>
    <div class="flourish flourish--bottom" role="img" aria-label="Purple scroll ornament"></div>
    <p class="signoff">Dorian Vellum</p>
  </section>

  <section class="card card--back" aria-label="Welcome card, brand side">
    <div class="card__pattern" role="img" aria-label="Border of small pink and black hexagon pattern"></div>
    <div class="card__panel"></div>
    <p class="brand-name">Dorian Vellum</p>
    <p class="web-address">WWW.DORIANVELLUM.EXAMPLE</p>
    <p class="social-names">Chatterbook<br>Snapgrove</p>
  </section>

</main>
</body>
</html>
```